label for a line of bbq rubs. my competition team name is copper skillet bbq *

i already have a logo, just need a label designed for a line of bbq rubs im developing. i want the design to be clean and eye catching and my colors of my logo are black and white. these will be sold in bbq specialty stores. i have a lot of traction in the bbq competition community, they are all familiar with my logo, just need a design that will stand out and draw attention to buys online and in the stores

Target Market(s)

backyard bbq cooks

Industry/Entity Type

Food blog

Font styles to use
Sans Serif

Colors

Designer to choose only greyscale colors for use in the design.

Requirements
Must have
• project must be simple, clean, with a classic look
Nice to have
• my logo, clean and simple

i have include some examples from other companies
Should not have
• cartoons

```html
<!DOCTYPE html>
<html lang="en">
<head>
<meta charset="utf-8">
<title>Copper Skillet BBQ – Rub Label</title>
<link rel="stylesheet" href="https://fonts.googleapis.com/css2?family=Lato:wght@300;400;700&family=Archivo:wght@400;700;900&display=swap">
<style>
  :root{
    --stage:#9d9fa2;
    --label:#000000;
    --ink:#ffffff;
    --panel:#ffffff;
    --panel-ink:#000000;
    --meat-light:#d08a4e;
    --meat-dark:#7a3a1a;
  }
  *{box-sizing:border-box;margin:0;padding:0}
  html,body{width:1146px;height:1200px;overflow:hidden}
  body{background:var(--stage);position:relative;font-family:"Lato",sans-serif}
  .label{position:absolute;left:33px;top:428px;width:1080px;height:344px;background:var(--label);color:var(--ink)}
  .abs{position:absolute}

  /* back panel */
  .back-title{left:27px;top:30px;font-size:14px;font-weight:400;letter-spacing:.3px}
  .copy{font-size:10.3px;line-height:12.6px;text-align:justify;width:308px;left:27px}
  .copy-1{top:58px}
  .copy-boxed{top:131px;width:308px;height:53px;border:1.6px solid var(--ink);padding:6px 7px}
  .copy-3{top:203px}
  .date{font-size:10px;left:175px}
  .issue{top:256px}
  .exp{top:289px}

  /* front panel */
  .brand-name{left:412px;top:44px;width:259px;font-family:"Lato",sans-serif;font-weight:700;
    font-size:46px;line-height:50px;letter-spacing:.5px;color:var(--ink);text-transform:uppercase}
  .flavours{left:412px;top:216px;font-size:18.5px;font-weight:400;line-height:22.5px}
  .net-wt{left:412px;top:289px;height:24px;padding:0 6px;background:var(--ink);color:var(--label);font-size:12px;font-weight:700;line-height:24px}
  .food-photo{left:508px;top:215px;width:164px;height:104px;border-radius:45% 40% 50% 45%;
    background:radial-gradient(ellipse at 40% 40%,var(--meat-light),var(--meat-dark) 80%)}

  /* badges */
  .badge{left:728px;width:90px;text-align:center;font-size:9.5px;white-space:nowrap}
  .badge svg{display:block;margin:0 auto 5px}
  .b1{top:42px}.b2{top:111px}.b3{top:180px}.b4{top:249px}

  /* nutrition */
  .nutrition{left:822px;top:28px;width:219px;height:286px;background:var(--panel);color:var(--panel-ink);padding:3px;font-family:"Archivo",sans-serif}
  .nf-frame{border:1px solid var(--panel-ink);height:100%;padding:2px 4px;font-size:8px;line-height:10.6px}
  .nf-title{font-size:21px;font-weight:900;letter-spacing:1.4px;line-height:21px}
  .nf-bar{height:5px;background:var(--panel-ink);margin:1px 0}
  .nf-thin{border-top:.8px solid var(--panel-ink)}
  .row{display:flex;justify-content:space-between;border-top:.8px solid var(--panel-ink)}
  .row b{font-weight:700}
  .indent{padding-left:12px}
  .small{font-size:6.4px;line-height:8px}
  .tiny-table{display:grid;grid-template-columns:72px 42px 42px 1fr;font-size:6.4px;line-height:8.6px}
  .right{text-align:right;font-weight:700}
</style>
</head>
<body>
<main class="label">
  <section class="back-panel">
    <h2 class="abs back-title">LOREM IPSUM</h2>
    <p class="abs copy copy-1">Lorem ipsum dolor sit amet, consectetuer adipiscing elit, sed diam nonummy nibh euismod tincidunt ut laoreet dolore magna aliquam erat volutpat. Ut wisi enim ad minim veniam, quis nostrud exerci tation ullamcorper suscipit lobortis nisl ut aliquip ex ea commodo consequat. Duis autem vel eum iriure dolor.</p>
    <p class="abs copy copy-boxed">Lorem ipsum dolor sit amet, consectetuer adipiscing elit, sed diam nonummy nibh euismod tincidunt ut laoreet dolore magna aliquam erat volutpat. Ut wisi enim ad minim veniam.</p>
    <p class="abs copy copy-3">Lorem ipsum dolor sit amet, consectetuer adipiscing elit, sed diam nonummy nibh euismod tincidunt ut laoreet dolore magna aliquam erat volutpat. Ut wisi enim ad minim veniam</p>
    <p class="abs date issue">Issue Date:</p>
    <p class="abs date exp">Exp Date:</p>
  </section>

  <section class="front-panel">
    <h1 class="abs brand-name">Copper<br>Skillet<br>BBQ</h1>
    <p class="abs flavours">BRISKET,<br>RIBS &amp;<br>CHICKEN</p>
    <div class="abs food-photo" role="img" aria-label="Photo of glazed barbecue chicken drumsticks"></div>
    <p class="abs net-wt">Net wt 11 0z (312g)</p>
  </section>

  <section class="badges">
    <div class="abs badge b1"><svg width="36" height="36"><circle cx="18" cy="18" r="16" fill="none" stroke="#fff" stroke-width="2"/></svg>Gluten Free</div>
    <div class="abs badge b2"><svg width="36" height="36"><circle cx="18" cy="18" r="16" fill="none" stroke="#fff" stroke-width="2"/></svg>Non GMO</div>
    <div class="abs badge b3"><svg width="36" height="36"><circle cx="18" cy="18" r="16" fill="none" stroke="#fff" stroke-width="2"/></svg>Halal Certified</div>
    <div class="abs badge b4"><svg width="36" height="36"><circle cx="18" cy="18" r="16" fill="none" stroke="#fff" stroke-width="2"/></svg>Kosher Certified</div>
  </section>

  <section class="abs nutrition">
    <div class="nf-frame">
      <div class="nf-title">Nutrition Facts</div>
      <div>Serving Size 1 (44g)</div>
      <div class="nf-bar"></div>
      <div class="small"><b>Amount Per Serving</b></div>
      <div class="nf-thin"><b>Calories</b> 96</div>
      <div class="nf-bar" style="height:3px"></div>
      <div class="small right">% Daily Values*</div>
      <div class="row"><span><b>Total Fat</b> 1g</span><b>2%</b></div>
      <div class="row indent"><span>Saturated Fat 0g</span><b>0%</b></div>
      <div class="row indent"><span>Trans Fat 0g</span><span></span></div>
      <div class="row"><span><b>Cholesterol</b> 0mg</span><b>0%</b></div>
      <div class="row"><span><b>Sodium</b> 1mg</span><b>0%</b></div>
      <div class="row"><span><b>Total Carbohydrate</b> 22g</span><b>7%</b></div>
      <div class="row indent"><span>Dietary Fiber 0g</span><b>0%</b></div>
      <div class="row indent"><span>Sugars 6g</span><span></span></div>
      <div class="row"><span><b>Protein</b> 1g</span><b>2%</b></div>
      <div class="nf-bar" style="height:3px"></div>
      <p class="small">*Percent Daily Values are based on a 2,000 calorie diet. Your Daily Values may be higher or lower depending on your calorie needs.</p>
      <div class="tiny-table nf-thin">
        <span></span><span>Calories</span><span>2,000</span><span>2,500</span>
        <span>Total Fat</span><span>Less than</span><span>65g</span><span>80g</span>
        <span>Sat Fat</span><span>Less than</span><span>20g</span><span>25g</span>
        <span>Cholesterol</span><span>Less than</span><span>300mg</span><span>300mg</span>
        <span>Sodium</span><span>Less than</span><span>2400mg</span><span>2400mg</span>
        <span>Total Carbohydrate</span><span></span><span>300g</span><span>375g</span>
        <span>Dietary Fiber</span><span></span><span>25g</span><span>30g</span>
      </div>
    </div>
  </section>
</main>
</body>
</html>
```